Tallgrove Vale Management

I need a professional website. My current website is tallgrovevalemanagement.com and I hate it. It was created with some AI tool very quickly because I needed a site up and running with no advanced notice. I’m open to all designs .. I trust you, the professionals will deliver the results I’m anxiously awaiting! :)

```html
<!DOCTYPE html>
<html lang="en">
<head>
<meta charset="utf-8">
<title>Tallgrove Vale Management</title>
<link href="https://fonts.googleapis.com/css2?family=Montserrat:wght@400;500;600;700&family=Roboto:wght@500;700&display=swap" rel="stylesheet">
<style>
:root{
  --navy:#233a66;
  --navy-dark:#1f3461;
  --red:#b8222a;
  --red-band:#c9353b;
  --gold:#b08d62;
  --text:#2b2b2b;
  --muted:#555;
  --light:#f2f2f3;
  --white:#fff;
}
*{box-sizing:border-box;margin:0;padding:0}
html,body{width:1200px;height:4113px;overflow:hidden}
body{position:relative;font-family:"Montserrat",sans-serif;color:var(--text);background:var(--white)}
.abs{position:absolute}
.btn{position:absolute;display:flex;align-items:center;justify-content:center;background:var(--red);color:var(--white);font-family:"Montserrat",sans-serif;font-weight:700;font-size:14px;letter-spacing:.2px;text-transform:uppercase}
.heading{font-family:"Roboto",sans-serif;font-weight:700;color:var(--navy);text-transform:uppercase}
.underline{position:absolute;height:3px;background:var(--red)}

/* header + hero */
.hero-photo{left:0;top:0;width:1200px;height:686px;background:linear-gradient(100deg,#eef0f3 0%,#e9ebee 45%,#e2ddd6 70%,#c9b7a3 100%)}
.nav a{position:absolute;top:73px;font-size:15px;font-weight:600;color:var(--navy);text-decoration:none;text-transform:uppercase}
.nav a.active{color:var(--red);border-bottom:2px solid var(--red);padding-bottom:1px}
.brand{position:absolute;left:500px;top:44px;width:200px;text-align:center;font-family:"Montserrat",sans-serif;font-weight:700;font-size:17px;line-height:22px;color:var(--navy);text-transform:uppercase}
.hero-title{left:200px;top:222px;width:800px;text-align:center;font-size:48px;line-height:57px}
.hero-text{left:255px;top:347px;width:690px;text-align:center;font-size:20px;line-height:28.5px;color:#222}

/* about */
.about-brand{left:110px;top:820px;width:488px;height:500px;display:flex;flex-direction:column;align-items:center;justify-content:center;gap:28px}
.about-brand .mark{width:120px;height:120px;background:var(--navy)}
.about-brand .name{font-family:"Montserrat",sans-serif;font-weight:700;font-size:46px;line-height:56px;color:var(--navy);text-align:center;text-transform:uppercase}
.about-title{left:661px;top:812px;font-size:41px}
.about-text{left:661px;top:890px;width:428px;font-size:16.5px;line-height:25.7px;text-align:justify;color:#333}
.about-text p+p{margin-top:15px}
.photo-back{left:488px;top:1494px;width:592px;height:351px;background:linear-gradient(160deg,#7e8a4f 0%,#5d6b36 40%,#a79c86 75%,#6f6a60 100%)}
.photo-front{left:112px;top:1368px;width:479px;height:359px;border:8px solid var(--white);background:linear-gradient(135deg,#8d8b88 0%,#6f6c69 40%,#c9a77b 70%,#e6dccd 100%)}
.frame{border-color:var(--gold);border-style:solid}

/* services */
.services{left:0;top:1979px;width:1200px;height:619px;background:var(--light)}
.services-title{left:0;top:2058px;width:1200px;text-align:center;font-size:41px}
.card{position:absolute;top:2158px;width:229px;height:351px;background:var(--white);box-shadow:0 2px 10px rgba(0,0,0,.05);text-align:center}
.card.featured{background:var(--navy)}
.card .icon{position:absolute;left:70px;top:30px}
.card h3{position:absolute;left:0;top:136px;width:100%;font-size:15.5px;font-weight:700;color:var(--navy);text-transform:uppercase}
.card p{position:absolute;left:14px;top:164px;width:201px;font-size:14.5px;line-height:23px;color:#444}
.card.featured h3,.card.featured p{color:var(--white)}
.card .btn{left:42px;top:274px;width:145px;height:44px}
.card.featured .btn{background:var(--white);color:var(--red)}

/* testimonials */
.testimonials{left:0;top:2598px;width:1200px;height:583px;background:linear-gradient(110deg,#c4323a 0%,#d23b40 50%,#c02e35 100%)}
.testimonials-title{left:0;top:2667px;width:1200px;text-align:center;font-size:41px;color:var(--white)}
.quote-card{position:absolute;top:2758px;width:300px;height:300px;background:var(--white);border-radius:8px}
.quote-card .qm{position:absolute;left:14px;top:20px;font-family:"Roboto",sans-serif;font-weight:700;font-size:56px;line-height:56px;color:var(--navy)}
.quote-card .stars{position:absolute;left:30px;top:64px}
.quote-card p{position:absolute;left:30px;top:98px;width:250px;font-size:16px;line-height:22.4px;color:#222}
.quote-card .by{position:absolute;left:30px;top:256px;font-size:15px;font-weight:700;color:var(--navy)}
.dots{left:565px;top:3097px;display:flex;gap:10px}
.dots span{width:6px;height:6px;border-radius:50%;background:rgba(255,255,255,.55)}
.dots span.on{background:var(--white)}

/* contact */
.contact-title{left:0;top:3287px;width:1200px;text-align:center;font-size:41px}
.field{position:absolute;left:182px;width:407px;height:49px;background:var(--white);border-radius:22px;box-shadow:0 2px 10px rgba(0,0,0,.09);display:flex;align-items:center}
.field .ico{width:53px;height:100%;display:flex;align-items:center;justify-content:center;border-right:1px solid #e3e3e3}
.field span{padding-left:16px;font-size:15px;color:#333}
.message{position:absolute;left:606px;top:3379px;width:411px;height:180px;background:var(--white);border-radius:22px;box-shadow:0 2px 10px rgba(0,0,0,.09)}
.message .ico{position:absolute;left:0;top:12px;width:53px;height:40px;display:flex;align-items:center;justify-content:center;border-right:1px solid #e3e3e3}
.message span{position:absolute;left:68px;top:24px;font-size:15px;color:#333}

/* footer */
.footer{left:0;top:3728px;width:1200px;height:385px;background:var(--navy-dark)}
.footer-badge{left:110px;top:3830px;width:158px;height:158px;background:var(--white);clip-path:polygon(50% 0,100% 25%,100% 75%,50% 100%,0 75%,0 25%);display:flex;align-items:center;justify-content:center;text-align:center;font-weight:700;font-size:15px;line-height:19px;color:var(--navy);text-transform:uppercase}
.foot-head{position:absolute;top:3793px;font-size:15.5px;font-weight:700;color:var(--white);text-transform:uppercase}
.foot-head::after{content:"";position:absolute;left:0;top:28px;width:100%;height:3px;background:var(--red)}
.foot-item{position:absolute;left:308px;display:flex;align-items:center;gap:18px;color:var(--white);font-size:14px;line-height:22px}
.foot-item .dot{width:36px;height:36px;border-radius:50%;background:var(--white);display:flex;align-items:center;justify-content:center;flex:none}
.links a{position:absolute;left:660px;font-size:14.5px;color:var(--white);text-decoration:none}
.news{left:830px;top:3862px;width:258px;height:45px;background:var(--white);border-radius:3px;display:flex;align-items:center;justify-content:space-between;padding:0 16px;font-size:13.5px;color:#333}
.social{position:absolute;top:3934px;width:32px;height:32px;border-radius:50%;background:var(--white)}
.social.on{background:var(--red)}
.foot-rule{left:0;top:4049px;width:1200px;height:1px;background:rgba(255,255,255,.15)}
.copy{left:0;top:4066px;width:1200px;text-align:center;font-size:13px;color:var(--white)}
</style>
</head>
<body>

<!-- Hero -->
<div class="abs hero-photo" role="img" aria-label="Photo of a small model house beside a glass jar of coins on a soft light background"></div>
<nav class="nav">
  <a class="active" href="#" style="left:110px">Home</a>
  <a href="#" style="left:196px">About Us</a>
  <a href="#" style="left:316px">Our Services</a>
  <a href="#" style="left:755px">Contact Us</a>
</nav>
<div class="brand">Tallgrove Vale<br>Management</div>
<div class="btn" style="left:900px;top:59px;width:188px;height:46px">Request a Quote</div>

<h1 class="abs heading hero-title">A True Partner, Not Just<br>A Vendor.</h1>
<p class="abs hero-text">The organization applies rigorously tested frameworks and data-driven methodologies to safeguard property value while elevating tenant experience.</p>
<div class="btn" style="left:527px;top:450px;width:145px;height:45px">Contact Us</div>

<!-- About -->
<div class="abs about-brand">
  <div class="mark"></div>
  <div class="name">Tallgrove Vale<br>Management</div>
</div>
<h2 class="abs heading about-title">About Us</h2>
<div class="underline" style="left:661px;top:859px;width:76px"></div>
<div class="abs about-text">
  <p>Our organization delivers comprehensive property management solutions that optimize asset performance and tenant satisfaction. By integrating advanced analytics with proven operational frameworks, our specialists ensure each property achieves sustained value appreciation.</p>
  <p>Drawing on decades of collective expertise, the team facilitates regulatory compliance, cost efficiency, and proactive maintenance. This disciplined approach enables owners to preserve capital, enhance occupancy rates, and demonstrate long-term resilience across diverse market conditions.</p>
</div>
<div class="btn" style="left:661px;top:1270px;width:145px;height:45px">Learn More</div>

<div class="abs frame" style="left:592px;top:1422px;width:193px;height:62px;border-width:5px 5px 0 0"></div>
<div class="abs frame" style="left:350px;top:1728px;width:129px;height:64px;border-width:0 0 5px 5px"></div>
<div class="abs photo-back" role="img" aria-label="Photo of a small tree growing from stacked coins beside a model house"></div>
<div class="abs photo-front" role="img" aria-label="Photo of two professionals meeting at a table with a wooden model house and documents"></div>

<!-- Services -->
<div class="abs services"></div>
<h2 class="abs heading services-title">Services Offered</h2>
<div class="underline" style="left:562px;top:2105px;width:76px"></div>

<div class="card" style="left:112px">
  <svg class="icon" width="89" height="89" viewBox="0 0 89 89"><polygon points="44.5,2 82,23 82,66 44.5,87 7,66 7,23" fill="#fbe9ea"/><polygon points="44.5,22 64,33 64,56 44.5,67 25,56 25,33" fill="#b8222a"/><path d="M34 47 L44.5 37 L55 47 M37 45 V54 H52 V45" fill="none" stroke="#fff" stroke-width="3"/></svg>
  <h3>Property Care</h3>
  <p>Describe important details like price, value, length of service, and why it's unique.</p>
  <div class="btn">Learn More</div>
</div>
<div class="card" style="left:361px">
  <svg class="icon" width="89" height="89" viewBox="0 0 89 89"><polygon points="44.5,2 82,23 82,66 44.5,87 7,66 7,23" fill="#fbe9ea"/><path d="M32 46 L44.5 34 L57 46 M36 44 V56 H53 V44" fill="none" stroke="#b8222a" stroke-width="3"/><circle cx="44.5" cy="48" r="3.5" fill="#b8222a"/></svg>
  <h3>Tenant Services</h3>
  <p>Describe important details like price, value, length of service, and why it's unique.</p>
  <div class="btn">Learn More</div>
</div>
<div class="card featured" style="left:611px">
  <svg class="icon" width="89" height="89" viewBox="0 0 89 89"><polygon points="44.5,2 82,23 82,66 44.5,87 7,66 7,23" fill="#b8222a"/><circle cx="44.5" cy="44.5" r="14" fill="none" stroke="#fff" stroke-width="3"/><circle cx="44.5" cy="44.5" r="5" fill="#fff"/></svg>
  <h3>Maintenance</h3>
  <p>Describe important details like price, value, length of service, and why it's unique.</p>
  <div class="btn">Learn More</div>
</div>
<div class="card" style="left:860px">
  <svg class="icon" width="89" height="89" viewBox="0 0 89 89"><polygon points="44.5,2 82,23 82,66 44.5,87 7,66 7,23" fill="#fbe9ea"/><path d="M30 56 L40 46 L47 52 L59 38 M52 38 H59 V45" fill="none" stroke="#b8222a" stroke-width="3.5"/></svg>
  <h3>Investment Growth</h3>
  <p>Describe important details like price, value, length of service, and why it's unique.</p>
  <div class="btn">Learn More</div>
</div>

<!-- Testimonials -->
<div class="abs testimonials" role="img" aria-label="Red-tinted photo of a house behind the testimonials"></div>
<h2 class="abs heading testimonials-title">Testimonials</h2>
<div class="underline" style="left:562px;top:2714px;width:76px;background:#fff"></div>

<div class="quote-card" style="left:112px">
  <div class="qm">&ldquo;</div>
  <svg class="stars" width="106" height="18" viewBox="0 0 106 18"><g fill="#b8222a"><polygon points="9,0 11.6,6 18,6.5 13,10.7 14.6,17 9,13.6 3.4,17 5,10.7 0,6.5 6.4,6"/><polygon transform="translate(22 0)" points="9,0 11.6,6 18,6.5 13,10.7 14.6,17 9,13.6 3.4,17 5,10.7 0,6.5 6.4,6"/><polygon transform="translate(44 0)" points="9,0 11.6,6 18,6.5 13,10.7 14.6,17 9,13.6 3.4,17 5,10.7 0,6.5 6.4,6"/><polygon transform="translate(66 0)" points="9,0 11.6,6 18,6.5 13,10.7 14.6,17 9,13.6 3.4,17 5,10.7 0,6.5 6.4,6"/><polygon transform="translate(88 0)" points="9,0 11.6,6 18,6.5 13,10.7 14.6,17 9,13.6 3.4,17 5,10.7 0,6.5 6.4,6"/></g></svg>
  <p>Lorem ipsum dolor sit amet, conse ctetur adipiscing elit, sed do eiusm od tempor incididunt ut labore et dolore magna aliqua. Ut enim ad minim veniam, quisea.</p>
  <div class="by">- John Doe</div>
</div>
<div class="quote-card" style="left:450px">
  <div class="qm">&ldquo;</div>
  <svg class="stars" width="106" height="18" viewBox="0 0 106 18"><g fill="#b8222a"><polygon points="9,0 11.6,6 18,6.5 13,10.7 14.6,17 9,13.6 3.4,17 5,10.7 0,6.5 6.4,6"/><polygon transform="translate(22 0)" points="9,0 11.6,6 18,6.5 13,10.7 14.6,17 9,13.6 3.4,17 5,10.7 0,6.5 6.4,6"/><polygon transform="translate(44 0)" points="9,0 11.6,6 18,6.5 13,10.7 14.6,17 9,13.6 3.4,17 5,10.7 0,6.5 6.4,6"/><polygon transform="translate(66 0)" points="9,0 11.6,6 18,6.5 13,10.7 14.6,17 9,13.6 3.4,17 5,10.7 0,6.5 6.4,6"/><polygon transform="translate(88 0)" points="9,0 11.6,6 18,6.5 13,10.7 14.6,17 9,13.6 3.4,17 5,10.7 0,6.5 6.4,6"/></g></svg>
  <p>Lorem ipsum dolor sit amet, conse ctetur adipiscing elit, sed do eiusm od tempor incididunt ut labore et dolore magna aliqua. Ut enim ad minim veniam, quisea.</p>
  <div class="by">- John Doe</div>
</div>
<div class="quote-card" style="left:788px">
  <div class="qm">&ldquo;</div>
  <svg class="stars" width="106" height="18" viewBox="0 0 106 18"><g fill="#b8222a"><polygon points="9,0 11.6,6 18,6.5 13,10.7 14.6,17 9,13.6 3.4,17 5,10.7 0,6.5 6.4,6"/><polygon transform="translate(22 0)" points="9,0 11.6,6 18,6.5 13,10.7 14.6,17 9,13.6 3.4,17 5,10.7 0,6.5 6.4,6"/><polygon transform="translate(44 0)" points="9,0 11.6,6 18,6.5 13,10.7 14.6,17 9,13.6 3.4,17 5,10.7 0,6.5 6.4,6"/><polygon transform="translate(66 0)" points="9,0 11.6,6 18,6.5 13,10.7 14.6,17 9,13.6 3.4,17 5,10.7 0,6.5 6.4,6"/><polygon transform="translate(88 0)" points="9,0 11.6,6 18,6.5 13,10.7 14.6,17 9,13.6 3.4,17 5,10.7 0,6.5 6.4,6"/></g></svg>
  <p>Lorem ipsum dolor sit amet, conse ctetur adipiscing elit, sed do eiusm od tempor incididunt ut labore et dolore magna aliqua. Ut enim ad minim veniam, quisea.</p>
  <div class="by">- John Doe</div>
</div>
<div class="abs dots"><span></span><span></span><span></span><span class="on"></span><span></span></div>

<!-- Contact -->
<h2 class="abs heading contact-title">Contact Us</h2>
<div class="underline" style="left:562px;top:3334px;width:76px"></div>

<div class="field" style="top:3379px">
  <div class="ico"><svg width="14" height="16" viewBox="0 0 14 16"><circle cx="7" cy="4" r="4" fill="#233a66"/><path d="M0 16 C0 10 14 10 14 16 Z" fill="#233a66"/></svg></div>
  <span>Your Name</span>
</div>
<div class="field" style="top:3445px">
  <div class="ico"><svg width="16" height="12" viewBox="0 0 16 12"><rect width="16" height="12" rx="1.5" fill="#233a66"/><path d="M1 1 L8 7 L15 1" fill="none" stroke="#fff" stroke-width="1.4"/></svg></div>
  <span>Email</span>
</div>
<div class="field" style="top:3510px">
  <div class="ico"><svg width="15" height="15" viewBox="0 0 15 15"><path d="M3 0 L6 4 L4.5 6 C5.5 8 7 9.5 9 10.5 L11 9 L15 12 L13 15 C6 14 1 9 0 2 Z" fill="#233a66"/></svg></div>
  <span>Phone</span>
</div>
<div class="message">
  <div class="ico"><svg width="18" height="14" viewBox="0 0 18 14"><ellipse cx="7" cy="5.5" rx="7" ry="5" fill="#233a66"/><ellipse cx="12" cy="8.5" rx="6" ry="4.5" fill="#233a66"/></svg></div>
  <span>Your Message</span>
</div>
<div class="btn" style="left:512px;top:3586px;width:176px;height:46px">Send Message</div>

<!-- Footer -->
<div class="abs footer"></div>
<div class="abs footer-badge">Tallgrove<br>Vale<br>Management</div>

<div class="foot-head" style="left:308px">Contact Us</div>
<div class="foot-item" style="top:3848px">
  <div class="dot"><svg width="12" height="16" viewBox="0 0 12 16"><path d="M6 0 C2.7 0 0 2.6 0 6 C0 10 6 16 6 16 C6 16 12 10 12 6 C12 2.6 9.3 0 6 0 Z" fill="#b8222a"/><circle cx="6" cy="6" r="2.2" fill="#fff"/></svg></div>
  <div>465, Lorum Ipsum Dolore,<br>RIVERTON - ASHFIELD</div>
</div>
<div class="foot-item" style="top:3912px">
  <div class="dot"><svg width="14" height="14" viewBox="0 0 15 15"><path d="M3 0 L6 4 L4.5 6 C5.5 8 7 9.5 9 10.5 L11 9 L15 12 L13 15 C6 14 1 9 0 2 Z" fill="#b8222a"/></svg></div>
  <div>Call Us:<br>+1 (555) 010 0188</div>
</div>
<div class="foot-item" style="top:3980px">
  <div class="dot"><svg width="15" height="11" viewBox="0 0 16 12"><rect width="16" height="12" rx="1.5" fill="#b8222a"/><path d="M1 1 L8 7 L15 1" fill="none" stroke="#fff" stroke-width="1.4"/></svg></div>
  <div>Email Us:<br>info@tallgrovevalemanagement.com</div>
</div>

<div class="foot-head" style="left:660px">Quick Links</div>
<div class="links">
  <a href="#" style="top:3857px">Home</a>
  <a href="#" style="top:3893px">About Us</a>
  <a href="#" style="top:3929px">Services</a>
  <a href="#" style="top:3965px">Projects</a>
  <a href="#" style="top:4001px">Contact Us</a>
</div>

<div class="foot-head" style="left:829px">Newsletter</div>
<div class="abs news"><span>Email Address</span><svg width="15" height="15" viewBox="0 0 16 16"><path d="M16 0 L0 7 L6 9 L8 15 Z" fill="#b8222a"/></svg></div>
<div class="social on" style="left:831px" aria-label="Social link"></div>
<div class="social" style="left:871px" aria-label="Social link"></div>
<div class="social" style="left:910px" aria-label="Social link"></div>

<div class="abs foot-rule"></div>
<div class="abs copy">Copyright © 2026 &nbsp;/&nbsp; All Rights Reserved &nbsp;/&nbsp; Privacy Policy</div>

</body>
</html>
```